Business card design needed

I need a business card design for a dog walking, dog minding and dog training business. Please refer to my website for the basic company colours and fonts I'm after. Planning on a double sided card, so all information doesn't need to be on the 'front' side.
Cheers

Industry/Entity Type

Dog Training

Contact Information for Business Card

Meadow Paws - happy hounds
Rua 0498307164
meadowpawsdemo.com.au
-walking
-holiday stays
-onsite care
-training and behavioural consultations

```html
<!DOCTYPE html>
<html lang="en">
<head>
<meta charset="utf-8">
<title>Meadow Paws – Business Card</title>
<link rel="stylesheet" href="https://fonts.googleapis.com/css2?family=Arimo&family=Courier+Prime:wght@700&family=Open+Sans&family=PT+Serif&display=swap">
<style>
  :root {
    --brand-red: #ec1c24;
    --ink: #111111;
    --paper: #ffffff;
    --frame: #1a1a1a;
    --paw-dark: #161616;
    --paw-mid: #3a3a3a;
    --motif-tone: #4a4a4a;
  }
  html, body {
    margin: 0;
    padding: 0;
    width: 1200px;
    height: 693px;
    overflow: hidden;
    background: var(--paper);
  }
  .card {
    position: relative;
    width: 1200px;
    height: 693px;
    box-sizing: border-box;
    border: 2px solid var(--frame);
    background: var(--paper);
    overflow: hidden;
  }
  .paw {
    position: absolute;
    width: 68px;
    height: 68px;
    border-radius: 16px;
    background: radial-gradient(circle at 50% 55%, var(--paw-mid), var(--paw-dark) 70%);
  }
  .paw--1 { left: 49px;  top: 65px; }
  .paw--2 { left: 124px; top: 209px; }
  .paw--3 { left: 51px;  top: 352px; }
  .paw--4 { left: 124px; top: 444px; }
  .paw--5 { left: 49px;  top: 568px; }

  .brand-name {
    position: absolute;
    left: 120px;
    top: 292px;
    margin: 0;
    font-size: 70px;
    line-height: 1;
    font-weight: 400;
    white-space: nowrap;
  }
  .brand-name__first {
    font-family: "PT Serif", Georgia, serif;
    color: var(--brand-red);
  }
  .brand-name__second {
    font-family: "Arimo", Arial, sans-serif;
    color: var(--ink);
  }
  .tagline {
    position: absolute;
    left: 142px;
    top: 370px;
    margin: 0;
    font-family: "Open Sans", Arial, sans-serif;
    font-size: 44px;
    line-height: 1;
    color: var(--brand-red);
    white-space: nowrap;
  }

  .heart-motif {
    position: absolute;
    left: 856px;
    top: 66px;
    width: 212px;
    height: 174px;
    background: radial-gradient(ellipse at 50% 50%, var(--motif-tone) 0%, rgba(74,74,74,0.55) 45%, rgba(255,255,255,0) 72%);
  }
  .side-band {
    position: absolute;
    left: 1074px;
    top: 45px;
    width: 81px;
    height: 603px;
    background: var(--brand-red);
  }
  .divider {
    position: absolute;
    left: 658px;
    top: 367px;
    width: 416px;
    height: 3px;
    background: var(--brand-red);
  }
  .divider--on-band {
    left: 1074px;
    width: 52px;
    background: var(--paper);
  }

  .role, .person, .contact {
    position: absolute;
    margin: 0;
    text-align: center;
    white-space: nowrap;
    line-height: 1;
  }
  .role {
    left: 681px;
    width: 400px;
    top: 308px;
    font-family: "Arimo", Arial, sans-serif;
    font-size: 44px;
    color: var(--ink);
  }
  .person {
    left: 664px;
    width: 400px;
    top: 390px;
    font-family: "Courier Prime", "Courier New", monospace;
    font-weight: 700;
    font-size: 62px;
    color: var(--brand-red);
  }
  .contact {
    left: 648px;
    width: 420px;
    font-family: "Open Sans", Arial, sans-serif;
    color: var(--ink);
  }
  .contact--phone { top: 501px; font-size: 37px; left: 654px; }
  .contact--web   { top: 548px; font-size: 31px; }
</style>
</head>
<body>
  <main class="card">
    <div class="paw paw--1" role="img" aria-label="Black paw print"></div>
    <div class="paw paw--2" role="img" aria-label="Black paw print"></div>
    <div class="paw paw--3" role="img" aria-label="Black paw print"></div>
    <div class="paw paw--4" role="img" aria-label="Black paw print"></div>
    <div class="paw paw--5" role="img" aria-label="Black paw print"></div>

    <h1 class="brand-name"><span class="brand-name__first">MEADOW</span> <span class="brand-name__second">PAWS</span></h1>
    <p class="tagline">happy hounds</p>

    <div class="heart-motif" role="img" aria-label="Heart shape made of many small black paw prints"></div>

    <div class="side-band"></div>
    <div class="divider"></div>
    <div class="divider divider--on-band"></div>

    <p class="role">Dog walker</p>
    <p class="person">Rua</p>
    <p class="contact contact--phone">0498307164</p>
    <p class="contact contact--web">meadowpawsdemo.com.au</p>
  </main>
</body>
</html>
```